computter lessons

new business venture [ self employed ] will register my business name as " KEYVORLAN "
what I will offer is :-
computer lessons for new beginners.
Initial set up and basic overview.
lessons per hour in the comfort of your own home.
special rates for customers aged 50+
First lesson is half price with no obligation for booking any further appointments.
a learning and training plan will be presented based on your requirements.
an appraisal update on your new skills.

contact info:-
0161 4970213
07700 900482
larkden@mervoxmail.com

```html
<!DOCTYPE html>
<html lang="en">
<head>
<meta charset="utf-8">
<title>KEYVORLAN Computer Training</title>
<link rel="stylesheet" href="https://fonts.googleapis.com/css2?family=Arimo:wght@400;700&family=Roboto:wght@300&display=swap">
<style>
  :root {
    --navy: #2a2660;
    --sky: #5bc8ef;
    --orange: #f7941d;
    --ink: #333333;
    --rule: #cfcfcf;
    --chip: #e2e2e0;
    --paper: #ffffff;
  }
  * { margin: 0; padding: 0; box-sizing: border-box; }
  html, body { width: 1200px; height: 851px; overflow: hidden; background: var(--paper); }
  .flyer {
    position: relative;
    width: 1200px;
    height: 851px;
    overflow: hidden;
    background: var(--paper);
    font-family: "Arimo", Arial, sans-serif;
    color: var(--ink);
  }

  /* brand block */
  .brand {
    position: absolute;
    left: 40px;
    top: 255px;
    width: 420px;
    display: flex;
    align-items: center;
    justify-content: center;
    gap: 18px;
  }
  .brand-dot {
    width: 40px; height: 40px;
    border-radius: 50%;
    background: var(--sky);
    flex: none;
  }
  .brand-name {
    font-weight: 700;
    font-size: 52px;
    line-height: 64px;
    letter-spacing: 3px;
    color: var(--navy);
  }
  .service-title {
    position: absolute;
    left: 40px;
    top: 466px;
    width: 420px;
    text-align: center;
    font-size: 44px;
    line-height: 65px;
    letter-spacing: 7px;
    color: var(--navy);
    text-transform: uppercase;
  }

  /* contact */
  .contact { position: absolute; left: 46px; }
  .contact-email { top: 625px; }
  .contact-phone { top: 733px; }
  .contact-icon {
    position: absolute;
    left: 0; top: 0;
    width: 60px; height: 60px;
    border-radius: 50%;
    background: var(--chip);
    display: flex; align-items: center; justify-content: center;
  }
  .contact-text {
    position: absolute;
    left: 80px;
    font-size: 20px;
    line-height: 30px;
    white-space: nowrap;
  }
  .contact-email .contact-text { top: 38px; }
  .contact-phone .contact-text { top: 33px; }
  .contact-text .indent { padding-left: 12px; }

  /* offer list */
  .offer-heading {
    position: absolute;
    left: 586px;
    top: 84px;
    font-family: "Roboto", Helvetica, sans-serif;
    font-weight: 300;
    font-size: 47px;
    line-height: 60px;
    color: #222;
    white-space: nowrap;
  }
  .bullet {
    position: absolute;
    width: 22px; height: 22px;
    border-radius: 50%;
    background: var(--orange);
    left: 542px;
  }
  .rule {
    position: absolute;
    left: 530px;
    width: 634px;
    height: 1px;
    background: var(--rule);
  }
  .offer-item {
    position: absolute;
    left: 586px;
    width: 515px;
    font-size: 25px;
    line-height: 38px;
  }
</style>
</head>
<body>
<main class="flyer">

  <div class="brand">
    <span class="brand-dot"></span>
    <span class="brand-name">KEYVORLAN</span>
  </div>
  <p class="service-title">Computer<br>Training</p>

  <div class="contact contact-email">
    <span class="contact-icon">
      <svg width="30" height="24" viewBox="0 0 30 24" aria-hidden="true">
        <path d="M1 9 L15 1 L29 9 V23 H1 Z" fill="#333"/>
        <path d="M1 9 L15 17 L29 9" fill="none" stroke="#e2e2e0" stroke-width="1.5"/>
      </svg>
    </span>
    <p class="contact-text">: larkden@mervoxmail.com</p>
  </div>

  <div class="contact contact-phone">
    <span class="contact-icon">
      <svg width="28" height="28" viewBox="0 0 24 24" aria-hidden="true">
        <path fill="#333" d="M6.6 10.8c1.4 2.8 3.8 5.1 6.6 6.6l2.2-2.2c.3-.3.7-.4 1-.2 1.1.4 2.3.6 3.6.6.6 0 1 .4 1 1V20c0 .6-.4 1-1 1C10.6 21 3 13.4 3 4c0-.6.4-1 1-1h3.5c.6 0 1 .4 1 1 0 1.3.2 2.5.6 3.6.1.3 0 .7-.2 1z"/>
      </svg>
    </span>
    <p class="contact-text">: 0161 4970213<br><span class="indent">07700 900482</span></p>
  </div>

  <span class="bullet" style="top:112px"></span>
  <h1 class="offer-heading">What I offer :</h1>
  <span class="rule" style="top:160px"></span>

  <span class="bullet" style="top:198px"></span>
  <p class="offer-item" style="top:192px">Computer lessons for new beginners.</p>
  <span class="rule" style="top:250px"></span>

  <span class="bullet" style="top:277px"></span>
  <p class="offer-item" style="top:269px">Initial set up and basic overview</p>

  <span class="bullet" style="top:353px"></span>
  <p class="offer-item" style="top:347px">Lessons per hour in the comfort of your own home.</p>
  <span class="rule" style="top:437px"></span>

  <span class="bullet" style="top:469px"></span>
  <p class="offer-item" style="top:463px">Special rates for customers aged 50+</p>
  <span class="rule" style="top:525px"></span>

  <span class="bullet" style="top:549px"></span>
  <p class="offer-item" style="top:541px">First lesson is half price with no obligation for booking any further appointments.</p>
  <span class="rule" style="top:640px"></span>

  <span class="bullet" style="top:668px"></span>
  <p class="offer-item" style="top:657px">A learning and training plan will be presented based on your requirements.</p>
  <span class="rule" style="top:755px"></span>

  <span class="bullet" style="top:782px"></span>
  <p class="offer-item" style="top:774px">An appraisal update on your new skills.</p>

</main>
</body>
</html>
```